maple crest homeworks KOVA

Looking for business card design that represents our company. we are maple crest homeworks and we dedicate our skills of home energy efficiency to our customer by providing energy solution to their energy problems.
HVAC
SOLAR
INSULLATION
LIGHTING
DUCT TESTING
KOVA RATING.

```html
<!DOCTYPE html>
<html lang="en">
<head>
<meta charset="utf-8">
<title>Maple Crest Homeworks – Business Card</title>
<link rel="stylesheet" href="https://fonts.googleapis.com/css2?family=Roboto:wght@400;500;700&display=swap">
<style>
  :root {
    --page: #e9e7e3;
    --card-white: #f7f7f7;
    --ink: #0b0b0b;
    --panel: #050505;
    --brand-box: #1c2420;
    --green: #7cc242;
    --blue: #29a8e0;
    --text-light: #f2f2f2;
  }
  * { box-sizing: border-box; margin: 0; padding: 0; }
  html, body { width: 1200px; height: 950px; overflow: hidden; }
  body {
    background: var(--page);
    font-family: "Roboto", Arial, sans-serif;
    position: relative;
  }
  .card {
    position: absolute;
    left: 250px;
    width: 700px;
    height: 400px;
    border-radius: 26px;
    overflow: hidden;
    box-shadow: 0 10px 30px rgba(0,0,0,.18);
  }
  .card--front { top: 50px; background: var(--card-white); }
  .card--back { top: 500px; background: var(--ink); }

  /* front */
  .contact-panel {
    position: absolute;
    top: -3px; right: -3px;
    width: 430px; height: 308px;
    background: var(--panel);
    border: 3px solid var(--green);
    border-bottom-left-radius: 22px;
    padding: 34px 30px 0 36px;
    color: var(--text-light);
  }
  .contact-name {
    color: var(--blue);
    font-size: 30px;
    font-weight: 500;
    letter-spacing: .5px;
    line-height: 1;
  }
  .contact-title {
    color: var(--green);
    font-size: 18px;
    font-weight: 500;
    margin-top: 6px;
  }
  .contact-address {
    font-size: 17px;
    line-height: 1.35;
    margin-top: 16px;
  }
  .contact-list { list-style: none; margin-top: 12px; }
  .contact-list li {
    display: flex; align-items: center; gap: 12px;
    font-size: 17px; line-height: 1.55;
  }
  .contact-icon { width: 16px; height: 16px; flex: none; }

  .brand-box {
    position: absolute;
    left: 30px; top: 230px;
    width: 226px; height: 100px;
    background: var(--brand-box);
    border: 3px solid var(--green);
    border-radius: 12px;
    padding: 0 14px;
    display: flex; align-items: center; gap: 12px;
  }
  .brand-name {
    color: var(--green);
    font-size: 22px;
    font-weight: 500;
    line-height: 1.2;
    text-transform: uppercase;
    letter-spacing: 1px;
  }
  .brand-dot {
    flex: none;
    width: 20px; height: 20px; border-radius: 50%;
    background: var(--blue);
  }

  /* back */
  .back-brand {
    position: absolute;
    top: 130px; left: 0; right: 0;
    display: flex; flex-direction: column; align-items: center; gap: 18px;
  }
  .back-brand .brand-dot { width: 60px; height: 60px; }
  .back-brand .brand-name { font-size: 28px; }
  .service-list {
    position: absolute;
    left: 34px; bottom: 30px;
    list-style: none;
    display: flex; gap: 10px;
    color: var(--text-light);
    font-size: 17px;
  }
  .service-list li::before {
    content: "";
    display: inline-block;
    width: 6px; height: 6px; border-radius: 50%;
    background: var(--blue);
    margin-right: 6px;
    vertical-align: middle;
  }
</style>
</head>
<body>

<section class="card card--front">
  <div class="brand-box">
    <span class="brand-dot"></span>
    <span class="brand-name">maple crest homeworks</span>
  </div>

  <div class="contact-panel">
    <h1 class="contact-name">DANA WHITLOCK</h1>
    <p class="contact-title">CEO/FOUNDER</p>
    <p class="contact-address">4120 Birchwood Court<br>Fairbanks, Alaska 99712</p>
    <ul class="contact-list">
      <li>
        <svg class="contact-icon" viewBox="0 0 16 16"><path d="M4 1l3 3-2 2c1 2 3 4 5 5l2-2 3 3-2 3C7 15 1 9 1 3z" fill="#29a8e0"/></svg>
        555 214 7730
      </li>
      <li>
        <svg class="contact-icon" viewBox="0 0 16 16"><rect x="4" y="1" width="8" height="14" rx="1.5" fill="none" stroke="#29a8e0" stroke-width="1.6"/></svg>
        555 368 0192
      </li>
      <li>
        <svg class="contact-icon" viewBox="0 0 16 16"><rect x="1" y="5" width="14" height="9" rx="1" fill="#29a8e0"/><rect x="4" y="1" width="8" height="4" fill="#29a8e0"/></svg>
        555 902 4481
      </li>
      <li>
        <svg class="contact-icon" viewBox="0 0 16 16"><rect x="1" y="3" width="14" height="10" rx="1" fill="#29a8e0"/><path d="M1 4l7 5 7-5" fill="none" stroke="#050505" stroke-width="1.4"/></svg>
        dana@maplecresthomeworks.com
      </li>
      <li>
        <svg class="contact-icon" viewBox="0 0 16 16"><circle cx="8" cy="8" r="7" fill="#29a8e0"/><path d="M1 8h14M8 1c-3 4-3 10 0 14M8 1c3 4 3 10 0 14" fill="none" stroke="#050505" stroke-width="1"/></svg>
        www.maplecresthomeworks.com
      </li>
    </ul>
  </div>
</section>

<section class="card card--back">
  <div class="back-brand">
    <span class="brand-dot"></span>
    <span class="brand-name">maple crest homeworks</span>
  </div>
  <ul class="service-list">
    <li>Insulation</li>
    <li>Lighting</li>
    <li>Duct Testing</li>
    <li>KOVA Rating.</li>
  </ul>
</section>

</body>
</html>
```